Create an awesome website for a medical clinic

This is a new website for a doctor's office. The site should be clean and modern, easy to navigate.

This is a wellness clinic, we want to help our clients have a healthy, active lifestyle. It should be friendly and inviting, and easy for them to call or schedule an appointment.

The site should be responsive and designed using the attached Bootstrap 3 PSD.

We will provide stock photos, until then please use stock photos from:

photoharvestbin.net or
lumapicturevault.net (preferred)

Some example sites of clean and modern designs that we like:

https://tarnelspine.example/
http://walkpastjoints.example/
http://feelingbrisker.example/

Also attached is a temporary logo you can use.
Updates

Reason: Thank you everyone for your great designs - we need a little more time so I'm extending the project.

Need extra days to review

Also, the colors in the new logo I just linked to are the final colors of the logo, so feel free to use any complimentary colors to it.

Hi everyone, The boss wants to change the layout of the site a little bit - here's the revised layout: https://www.filecrate.example/s/q8vn31kd2pxe74rt/memo%2011_29_2017.pdf?dl=0 And the graphic assets you can use are here: https://www.filecrate.example/s/q8vn31kd2pxe74rt/memo%2011_29_2017.pdf?dl=0 Feel free to change the background color of the "topbar", and change the icons of the "why people trust us" if you want, these are just temporary placeholders. Thanks for your patience and hard work!

Target Market(s)

People seeking medical treatment (wellness clinic)

Industry/Entity Type

Doctor

Number of Pages Required

1 page

Font styles to use
Sans Serif

Colors
0592cd
33a6d7
abd037
9bcb3c

Requirements
Must have
• The home page should have: a strong hero image/slideshow, clinic phone number should be prominent and at the top of the page (in the nav), a "what to expect" section (this is like a FAQs section - see attachment), and a strong call to action (a button to call or schedule an appointment).
• The what to expect section is useful so that prospective clients can determine if we're a good fit for them or not. It's a basic, first-step pre-qualification block of information.
• Social media icons which links to our social media profiles should be included.
Nice to have
• - Link to 3 most recent blog entries
• - Testimonials
• - How a multilevel nav menu looks.

```html
<!DOCTYPE html>
<html lang="en">
<head>
<meta charset="utf-8">
<title>Fernhill Wellness Clinic – Navigation States</title>
<link href="https://fonts.googleapis.com/css2?family=Montserrat:wght@400;500;600;700&display=swap" rel="stylesheet">
<style>
:root{
  --blue:#0592cd;
  --blue-dark:#1a7a9e;
  --blue-soft:#5fb6d6;
  --navy:#0c2a4f;
  --green:#9bcb3c;
  --grey-bg:#f4f4f4;
  --text:#222;
  --white:#fff;
}
*{box-sizing:border-box;margin:0;padding:0}
html,body{width:1200px;height:1200px;overflow:hidden}
body{position:relative;font-family:"Montserrat",Arial,sans-serif;color:var(--text);background:var(--white)}
.abs{position:absolute}

.intro{left:0;top:0;width:1200px;height:127px;background:var(--grey-bg)}
.intro-card{left:74px;top:0;width:303px;height:26px;background:var(--white);border-left:4px solid var(--green);box-shadow:0 3px 8px rgba(0,0,0,.06);font-size:12px;padding:0 0 0 16px;line-height:8px}
.intro-rule{left:450px;top:0;width:1px;height:26px;background:#ddd}
.intro-note{top:13px;font-size:13px}

.gallery{left:0;top:127px;width:1200px;height:277px;display:flex}
.gallery-photo{flex:1}
.p1{background:linear-gradient(135deg,#4a5a3a,#c9a889 55%,#e8e2da)}
.p2{background:linear-gradient(135deg,#e8d9b0,#d4b27a 50%,#efe6cc)}
.p3{background:linear-gradient(180deg,#a9cfd6,#cfe3e0 45%,#d8c4a2)}
.p4{background:linear-gradient(135deg,#e8e8e6,#b9c7d3 55%,#5a83b4)}

.enquiries{left:0;top:404px;width:1200px;height:60px;display:flex;justify-content:center;align-items:center;gap:31px;font-size:13px}

.nav-compact{left:0;top:464px;width:1200px;height:85px;background:var(--blue);display:flex;justify-content:center;align-items:center;gap:40px;color:var(--white);font-size:11px;font-weight:600;letter-spacing:1.3px;border-left:2px solid #0a7fb2}
.social{display:flex;gap:12px}
.social-dot{width:34px;height:34px;border-radius:50%;background:var(--white)}

.state-banner{left:0;top:549px;width:1200px;height:101px;background:var(--navy);color:var(--white);display:flex;justify-content:center;align-items:center;font-size:30px;font-weight:600;letter-spacing:3px}

.topbar{left:0;top:650px;width:1200px;height:45px;background:var(--grey-bg)}
.follow{left:73px;top:16px;font-size:11px;font-weight:500;letter-spacing:1.2px}
.follow-dots{left:295px;top:11px;display:flex;gap:8px}
.follow-dot{width:22px;height:22px;border-radius:50%;background:var(--blue-soft)}
.follow-dot.active{background:var(--blue)}
.appointment{left:883px;top:0;width:243px;height:45px;background:var(--blue-dark);color:var(--white);font-size:11px;font-weight:600;letter-spacing:1.4px;display:flex;align-items:center;justify-content:center}

.header{left:0;top:695px;width:1200px;height:99px;background:var(--white)}
.brand{left:73px;top:20px;display:flex;align-items:center;gap:8px}
.brand-square{width:14px;height:14px;background:var(--green)}
.brand-name{font-size:17px;font-weight:700;color:var(--blue);letter-spacing:.5px}
.contact-icon{width:43px;height:43px;background:var(--blue);display:flex;align-items:center;justify-content:center}
.contact-text{font-size:9px;letter-spacing:1.4px;line-height:14px}
.contact-text strong{font-size:11px;font-weight:600}

.nav-main{left:0;top:794px;width:1200px;height:60px;background:var(--blue);color:var(--white);font-size:13.5px;font-weight:600;letter-spacing:1.6px}
.nav-main span{position:absolute;top:0;height:60px;line-height:60px}
.nav-main .current{background:var(--blue-dark);padding:0 18px}

.hero{left:0;top:854px;width:1200px;height:346px;background:radial-gradient(ellipse at 72% 70%,#d9a07a 0%,#b78a62 25%,#8a9a68 55%,#5d7a48 100%)}
.dropdown{left:207px;top:854px;width:171px;height:134px;background:var(--blue-dark);color:var(--white);font-size:13.5px;font-weight:600;letter-spacing:1.5px;padding:12px 0 0 19px;line-height:29.5px}
.dropdown .hover{text-decoration:underline;text-underline-offset:4px}
.hero-caption{left:73px;top:1037px;width:359px;height:163px;background:rgba(95,170,200,.82);color:var(--white);font-size:27px;font-weight:500;letter-spacing:2.5px;text-align:center;line-height:30px;padding-top:44px}
</style>
</head>
<body>

<section class="intro abs">
  <div class="intro-card abs">laoreet erat id, lobortis arcu.</div>
  <div class="intro-rule abs"></div>
  <p class="intro-note abs" style="left:520px">Maecenas pulvinar urna et augue.</p>
  <p class="intro-note abs" style="left:863px">Maecenas pulvinar urna et augue.</p>
</section>

<section class="gallery abs">
  <div class="gallery-photo p1" role="img" aria-label="Couple in sun hats riding a bicycle together"></div>
  <div class="gallery-photo p2" role="img" aria-label="Young woman smiling in a sunny wheat field"></div>
  <div class="gallery-photo p3" role="img" aria-label="Group of friends jumping on a beach"></div>
  <div class="gallery-photo p4" role="img" aria-label="Man working on a laptop in a bright office"></div>
</section>

<div class="enquiries abs">
  <span>For all enquiries and referrals please contact us at:</span>
  <span>Phone: (555) 014-2290</span>
  <span>Fax: (555) 014-7731</span>
  <span>Email: hello@fernhillwellness.example</span>
</div>

<nav class="nav-compact abs">
  <span>HOME</span><span>ABOUT US</span><span>FOR PARENTS</span><span>FOR PROFESSIONALS</span><span>FOR TEENS</span><span>BLOG</span><span>CONTACT US</span>
  <div class="social"><div class="social-dot"></div><div class="social-dot"></div><div class="social-dot"></div></div>
</nav>

<div class="state-banner abs">TOP IS UNCLICKED - BOTTOM IS CLICKED</div>

<div class="topbar abs">
  <span class="follow abs">FOLLOW US ON SOCIAL MEDIA!</span>
  <div class="follow-dots abs"><div class="follow-dot"></div><div class="follow-dot active"></div><div class="follow-dot"></div></div>
  <div class="appointment abs">MAKE AN APPOINTMENT</div>
</div>

<header class="header abs">
  <div class="brand abs"><div class="brand-square"></div><span class="brand-name">Fernhill Wellness Clinic</span></div>
  <div class="contact-icon abs" style="left:722px;top:28px">
    <svg width="24" height="24" viewBox="0 0 24 24"><path fill="#fff" d="M6.6 10.8c1.4 2.8 3.8 5.1 6.6 6.6l2.2-2.2c.3-.3.7-.4 1-.2 1.1.4 2.3.6 3.6.6.6 0 1 .4 1 1V20c0 .6-.4 1-1 1C10.6 21 3 13.4 3 4c0-.6.4-1 1-1h3.5c.6 0 1 .4 1 1 0 1.3.2 2.5.6 3.6.1.3 0 .7-.2 1z"/></svg>
  </div>
  <div class="contact-text abs" style="left:781px;top:36px"><strong>(555) 014-2290</strong><br>FAX: (555) 014-7731</div>
  <div class="contact-icon abs" style="left:930px;top:28px">
    <svg width="22" height="26" viewBox="0 0 22 26"><path fill="#fff" d="M11 1a9 9 0 0 0-9 9c0 6.5 9 15 9 15s9-8.5 9-15a9 9 0 0 0-9-9zm0 12.5A3.5 3.5 0 1 1 11 6.5a3.5 3.5 0 0 1 0 7z"/></svg>
  </div>
  <div class="contact-text abs" style="left:990px;top:28px"><strong>SUITE 12, LEVEL 2</strong><br>48 ARDENT LANE<br>MARLOW BAY, FL 30999</div>
</header>

<nav class="nav-main abs">
  <span style="left:122px">HOME</span>
  <span class="current" style="left:207px">ABOUT US</span>
  <span style="left:360px">FOR PARENTS</span>
  <span style="left:523px">FOR PROFESSIONALS</span>
  <span style="left:743px">FOR TEENS</span>
  <span style="left:885px">BLOG</span>
  <span style="left:983px">CONTACT US</span>
</nav>

<section class="hero abs" role="img" aria-label="Smiling mature couple embracing outdoors"></section>

<div class="dropdown abs">
  <div>WHO WE ARE</div>
  <div>WHAT WE DO</div>
  <div class="hover">WHERE WE WORK</div>
  <div>OUR GOALS</div>
</div>

<div class="hero-caption abs">We specialise in<br>many areas,<br>find the right<br>clinic for you &amp;</div>

</body>
</html>
```